We are looking for a new PowerPoint template for our new CI

Hey artmingle! For 25 years we have been an owner-managed IT system house with tradition, values and a great team. After more than 10 years, we would like to upgrade our company and design the entire CI contemporary and modern. Therefore we are looking for a Powerpoint Template which fits to our logo, the colors and an IT company. Details about our company and our service portfolio can be found on our homepage. We are currently adapting our homepage to the new CI resulting from the logo revision. Homepage: http://stage.kovantra.de Color codes: Gray = RGB: 4040404040 White = RGB: F5F5F5F5F5 Orange = RGB: F7931E Our slogan: We keep your system running Our address data: Company = Kovantra GmbH Street = Lindbergstraße 12 POSTCODE = 71844 City = Burladingen We look forward to your ideas and thank you all in advance.

Target Market(s)

Our target group are companies with 10 to 100 employees from all industrial sectors, eg https://www.morvik-werke.de/ https://www.faltner-logistik.de/ https://www.quensel.de/ de /

Colors

Designer to choose colors to be used in the design.

Requirements
Must have
• We are looking for a modern IT design in gray / orange. The basis of the design should be our logo. The template should have two different layouts and three different layouts for content. Our logo and slogan should be clearly visible on the start layout. In addition, an area should be reserved for the name of a speaker and the occasion of the presentation.

```html
<!DOCTYPE html>
<html lang="de">
<head>
<meta charset="utf-8">
<title>Kovantra – Leistungsbereiche</title>
<link href="https://fonts.googleapis.com/css2?family=Noto+Sans:wght@400&display=swap" rel="stylesheet">
<style>
  :root {
    --orange: #F7931E;
    --card: #FFFFFF;
    --title: #404040;
    --body: #7A7A7A;
    --icon: #4A7EB0;
    --icon-halo: #FAFBFC;
  }
  * { box-sizing: border-box; margin: 0; padding: 0; }
  html, body {
    width: 1200px;
    height: 675px;
    overflow: hidden;
  }
  body {
    background: var(--orange);
    font-family: "Noto Sans", "Segoe UI", Arial, sans-serif;
  }
  .slide {
    position: relative;
    width: 1200px;
    height: 675px;
  }
  .service-card {
    position: absolute;
    top: 68px;
    width: 337px;
    height: 537px;
    background: var(--card);
    border-radius: 28px;
    box-shadow: 6px 10px 24px rgba(120, 60, 0, 0.22);
    text-align: center;
  }
  .service-card--systemhaus { left: 60px; }
  .service-card--software { left: 430px; }
  .service-card--praxis { left: 800px; }
  .service-icon {
    position: absolute;
    left: 50%;
    top: 82px;
    width: 84px;
    height: 84px;
    margin-left: -42px;
    border-radius: 50%;
    background: var(--icon-halo);
    display: flex;
    align-items: center;
    justify-content: center;
  }
  .service-icon svg {
    width: 64px;
    height: 64px;
    fill: none;
    stroke: var(--icon);
    stroke-width: 2.6;
    stroke-linecap: round;
    stroke-linejoin: round;
  }
  .service-title {
    position: absolute;
    top: 182px;
    left: 0;
    width: 100%;
    font-size: 21px;
    line-height: 30px;
    font-weight: 400;
    color: var(--title);
  }
  .service-text {
    position: absolute;
    top: 262px;
    left: 38px;
    right: 38px;
    font-size: 16px;
    line-height: 24px;
    color: var(--body);
  }
</style>
</head>
<body>
<main class="slide">
  <section class="service-card service-card--systemhaus">
    <div class="service-icon">
      <svg viewBox="0 0 66 66" aria-hidden="true">
        <circle cx="27" cy="27" r="9"/>
        <path d="M10 52c0-10 7.5-16 17-16s17 6 17 16"/>
        <path d="M38 15a8 8 0 1 1 5 14"/>
        <path d="M46 35c6 2 10 8 10 15"/>
      </svg>
    </div>
    <h2 class="service-title">IT Systemhaus</h2>
    <p class="service-text">Drei Säulen bilden die Basis für die Zufriedenheit unserer Kunden. Die individuelle IT-Beratung, perfekte IT-Lösungen für jeden Anspruch im Bereich Hard- und Software sowie IT-Service der über eine reine Systemwartung weit hinausgeht.</p>
  </section>

  <section class="service-card service-card--software">
    <div class="service-icon">
      <svg viewBox="0 0 66 66" aria-hidden="true">
        <polyline points="24,12 4,33 24,54"/>
        <polyline points="42,12 62,33 42,54"/>
      </svg>
    </div>
    <h2 class="service-title">Softwareschmiede</h2>
    <p class="service-text">Arbeitsschutz Management Software aus der Praxis für die Praxis<br>Ihre Vorgesetzten, Fachkräfte für Arbeitssicherheit, Administratoren und Kontrollorgane werden durch Kovantra unterstützt und entlastet.</p>
  </section>

  <section class="service-card service-card--praxis">
    <div class="service-icon">
      <svg viewBox="0 0 66 66" aria-hidden="true">
        <polyline points="10,58 10,46 24,46 24,36 38,36 38,24 54,24 54,58 10,58"/>
        <line x1="14" y1="30" x2="36" y2="8"/>
        <polyline points="24,8 36,8 36,20"/>
      </svg>
    </div>
    <h2 class="service-title">Medora Vita</h2>
    <p class="service-text">Die Praxissoftware Medora Vita ist die ideale Lösung für niedergelassene Ärzte. Sieger in den Kategorien Anwenderfreundlichkeit, Regionaler Support, Hotline Beratungsqualität und Erreichbarkeit.</p>
  </section>
</main>
</body>
</html>
```